辛味調味料のラベルをリニューアルし、一新したく思います。
同シリーズの2種のラベルデザインをお願いします。(柚子胡椒・赤おろし)
柚子胡椒は漢字・平仮名おまかせします。
どちらも、無添加・無着色です。

【柚子胡椒の原料】
香り良く鮮やかな青柚子、新鮮な青唐辛子・澄浦の塩(釜焚海水塩)です。

【赤おろしの原料】
新鮮な赤唐辛子・塩のみです。※柑橘不使用です。

新ラベルは以下のイメージでお願いします。
・和モダン又はスタイリッシュ
・掛紙不要のデザイン
・同シリーズなので2種に関連を持たせて下さい。
・デザインにより、紙ラベル・透明ラベルどちらでも可。
・弊社ロゴは、表のデザインに不要です。
・お召し上がり方は不要です。
・デザイン以外の部分(バーコード等・名称等~栄養成分表示)は変更なしです。

●現在の柚子胡椒
http://shop.kanemori-ichiba.example/fs/kanemori/yuzukosho/5182

●現在の赤おろし
http://shop.kanemori-ichiba.example/fs/kanemori/akaoroshi/5179
ラベル全体サイズ各:W138mm・H25mm(実質的なデザイン部分は、W75mm・H25mmです。
デザイン以外の箇所の変更はありません。(添付を参照)
カラー4色まで可・ロール

どれも素晴らしいデザインばかりでしたが、和の凛とした上品な雰囲気に魅せられました。
今回の辛味調味料について、私どもの考えるイメージと合致しておりましたので、こちらを当選とさせていただきました。
素晴らしいデザインの数々、本当にありがとうございました。

この度は、弊社の辛味調味料2種のラベルに多数のご応募・ご提案を頂き、誠にありがとうございます。
全てが素晴らしいデザインで甲乙つけ難いものばかりでした。
また、どれも自分ではデザインできないようなものばかりで、デザイナーの皆さまのレベルの高さを感じました。
今後もデザイナーの皆さまにご協力をお願いすることが出てくるかと思います。
今後ともどうぞよろしくお願いいたします。
本来であれば、お一人お一人にお礼を申し上げたいところですが、この場をおかりして心から感謝を申し上げます。
本当にありがとうございました。

```html
<!DOCTYPE html>
<html lang="ja">
<head>
<meta charset="utf-8">
<title>辛味調味料ラベル 赤おろし・柚子胡椒</title>
<link href="https://fonts.googleapis.com/css2?family=Shippori+Mincho:wght@600;800&family=Noto+Sans+JP:wght@400;500&display=swap" rel="stylesheet">
<style>
  :root{
    --bg:#ffffff;
    --paper:#ffffff;
    --ink:#333333;
    --rule:#9a9a9a;
    --red:#d8261c;
    --red-soft:#ec9a90;
    --red-pale:#fbe4e0;
    --red-deep:#b3160f;
    --green:#4f9a2e;
    --green-soft:#a9d38c;
    --green-pale:#eaf5e0;
    --green-deep:#3c7d20;
    --gold:#c9a64a;
  }
  *{margin:0;padding:0;box-sizing:border-box}
  html,body{width:840px;height:1200px;overflow:hidden;background:var(--bg)}
  body{position:relative;font-family:"Noto Sans JP",sans-serif;color:var(--ink)}

  .label{
    position:absolute;left:30px;width:780px;height:142px;
    background:var(--paper);border:1px solid #d6d6d6;
    display:flex;
  }
  .label--akaoroshi{top:300px;--accent:var(--red);--accent-deep:var(--red-deep)}
  .label--yuzukosho{top:760px;--accent:var(--green);--accent-deep:var(--green-deep)}

  .label__code-strip{width:26px;flex:none}
  .label__front{position:relative;width:396px;flex:none;overflow:hidden}
  .label__pattern{position:absolute;inset:0}
  .label--akaoroshi .label__pattern{
    background:linear-gradient(115deg,var(--red-soft) 0%,var(--red-pale) 30%,#fff 50%,var(--red-pale) 70%,var(--red-soft) 100%);
  }
  .label--yuzukosho .label__pattern{
    background:linear-gradient(115deg,var(--green-soft) 0%,var(--green-pale) 30%,#fff 50%,var(--green-pale) 70%,var(--green-soft) 100%);
  }

  .title-plate{
    position:absolute;left:50%;top:22px;transform:translateX(-50%);
    height:60px;padding:0 22px;background:var(--paper);
    border:2px solid var(--gold);outline:3px solid var(--accent);outline-offset:2px;
    display:flex;align-items:center;justify-content:center;white-space:nowrap;
  }
  .title-plate__name{
    font-family:"Shippori Mincho",serif;font-weight:800;font-size:32px;
    color:var(--accent-deep);letter-spacing:2px;white-space:nowrap;
  }
  .front__claim{
    position:absolute;left:0;right:0;top:98px;text-align:center;
    font-family:"Shippori Mincho",serif;font-weight:600;font-size:14px;
    color:var(--ink);letter-spacing:2px;
  }
  .front__stamp{
    position:absolute;left:10px;bottom:8px;width:58px;height:14px;background:var(--accent)
  }

  .label__info{
    flex:1;padding:12px 8px 6px 14px;font-size:8px;line-height:1.55;
    border-left:1px solid #e5e5e5;
  }
  .info__row{display:flex;white-space:nowrap}
  .info__key{width:50px;flex:none}
  .info__url{margin-top:2px}

  .label__nutrition{width:124px;flex:none;padding:12px 10px 0 0;font-size:7.4px}
  .nutrition__head{margin-bottom:3px;line-height:1.3;font-size:6.8px;white-space:nowrap}
  .nutrition__table{width:100%;border-collapse:collapse}
  .nutrition__table td{border:1px solid var(--rule);padding:1px 3px;line-height:1.3}
  .nutrition__table td:last-child{text-align:right}
</style>
</head>
<body>

<section class="label label--akaoroshi" aria-label="赤おろし ラベル">
  <div class="label__code-strip"></div>
  <div class="label__front">
    <div class="label__pattern" role="img" aria-label="赤唐辛子が散らばる模様"></div>
    <div class="title-plate"><span class="title-plate__name">赤おろし</span></div>
    <p class="front__claim">無添加・無着色</p>
    <div class="front__stamp"></div>
  </div>
  <div class="label__info">
    <div class="info__row"><span class="info__key">名　　称</span><span>：香辛料調味料</span></div>
    <div class="info__row"><span class="info__key">原材料名</span><span>：赤唐辛子、食塩</span></div>
    <div class="info__row"><span class="info__key">内 容 量</span><span>：80g</span></div>
    <div class="info__row"><span class="info__key">賞味期限</span><span>：下部に記載</span></div>
    <div class="info__row"><span class="info__key">保存方法</span><span>：直射日光・高温多湿を避け常温保存</span></div>
    <div class="info__row"><span class="info__key">製 造 者</span><span>：株式会社金森市場 澄浦町1-12-8</span></div>
    <div class="info__row"><span class="info__key"></span><span>　TEL 0000-12-3456</span></div>
    <div class="info__url">http://shop.kanemori-ichiba.example</div>
  </div>
  <div class="label__nutrition">
    <p class="nutrition__head">栄養成分表示 大さじ1杯(15g)当り</p>
    <table class="nutrition__table">
      <tr><td>エネルギー</td><td>7kcal</td></tr>
      <tr><td>たんぱく質</td><td>0.3g</td></tr>
      <tr><td>脂質</td><td>0.2g</td></tr>
      <tr><td>炭水化物</td><td>1.2g</td></tr>
      <tr><td>食塩相当量</td><td>2.4g</td></tr>
    </table>
  </div>
</section>

<section class="label label--yuzukosho" aria-label="柚子こしょう ラベル">
  <div class="label__code-strip"></div>
  <div class="label__front">
    <div class="label__pattern" role="img" aria-label="青唐辛子と柚子の葉が散らばる模様"></div>
    <div class="title-plate"><span class="title-plate__name">柚子こしょう</span></div>
    <p class="front__claim">無添加・無着色</p>
    <div class="front__stamp"></div>
  </div>
  <div class="label__info">
    <div class="info__row"><span class="info__key">名　　称</span><span>：柚子こしょう</span></div>
    <div class="info__row"><span class="info__key">原材料名</span><span>：青唐辛子、青柚子、澄浦の塩</span></div>
    <div class="info__row"><span class="info__key">内 容 量</span><span>：80g</span></div>
    <div class="info__row"><span class="info__key">賞味期限</span><span>：下部に記載</span></div>
    <div class="info__row"><span class="info__key">保存方法</span><span>：直射日光・高温多湿を避け常温保存</span></div>
    <div class="info__row"><span class="info__key">製 造 者</span><span>：株式会社金森市場 澄浦町1-12-8</span></div>
    <div class="info__row"><span class="info__key"></span><span>　TEL 0000-12-3456</span></div>
    <div class="info__url">http://shop.kanemori-ichiba.example</div>
  </div>
  <div class="label__nutrition">
    <p class="nutrition__head">栄養成分表示 大さじ1杯(15g)当り</p>
    <table class="nutrition__table">
      <tr><td>エネルギー</td><td>6kcal</td></tr>
      <tr><td>たんぱく質</td><td>0.2g</td></tr>
      <tr><td>脂質</td><td>0.1g</td></tr>
      <tr><td>炭水化物</td><td>1.3g</td></tr>
      <tr><td>食塩相当量</td><td>2.6g</td></tr>
    </table>
  </div>
</section>

</body>
</html>
```